Business Card Design

My business is writing crime novels to entertain readers. I write legal thrillers and mysteries. I need a card for publishers, agents, other authors, and media.

Industry/Entity Type

Legal

Contact Information for Business Card

Paul Ostrander
www.ostranderthrillers.example
paulbostrander@mailbox.example
0064 27 5139427

```html
<!DOCTYPE html>
<html lang="en">
<head>
<meta charset="utf-8">
<title>Paul Ostrander – Business Card</title>
<link href="https://fonts.googleapis.com/css2?family=Lato:wght@300;400&display=swap" rel="stylesheet">
<style>
  :root {
    --card-bg: #343b47;
    --text-light: #f5f6f7;
    --portrait-top: #5a5652;
    --portrait-mid: #2a2828;
    --portrait-bottom: #1a1a1a;
  }
  html, body {
    margin: 0;
    padding: 0;
    width: 1200px;
    height: 741px;
    overflow: hidden;
    background: var(--card-bg);
  }
  .card {
    position: relative;
    width: 1200px;
    height: 741px;
    background: var(--card-bg);
    font-family: "Lato", sans-serif;
    color: var(--text-light);
  }
  .portrait {
    position: absolute;
    left: 97px;
    top: 86px;
    width: 413px;
    height: 593px;
    background: linear-gradient(180deg, var(--portrait-top) 0%, var(--portrait-mid) 55%, var(--portrait-bottom) 100%);
  }
  .author-name {
    position: absolute;
    left: 595px;
    top: 358px;
    margin: 0;
    font-size: 78px;
    font-weight: 400;
    line-height: 1;
    letter-spacing: 0.5px;
    white-space: nowrap;
  }
  .contact-list {
    position: absolute;
    left: 598px;
    top: 516px;
    margin: 0;
    padding: 0;
    list-style: none;
  }
  .contact-item {
    display: flex;
    align-items: center;
    height: 60px;
    font-size: 32px;
    font-weight: 400;
    white-space: nowrap;
  }
  .contact-icon {
    width: 32px;
    height: 32px;
    margin-right: 32px;
    fill: var(--text-light);
    flex: none;
  }
  .contact-icon.outline {
    fill: none;
    stroke: var(--text-light);
    stroke-width: 2.2;
  }
</style>
</head>
<body>
  <main class="card">
    <div class="portrait" role="img" aria-label="Portrait photograph of the author in a dark leather jacket and white shirt"></div>

    <h1 class="author-name">Paul Ostrander</h1>

    <ul class="contact-list">
      <li class="contact-item">
        <svg class="contact-icon" viewBox="0 0 24 24" aria-hidden="true">
          <path d="M6.6 10.8c1.4 2.8 3.8 5.1 6.6 6.6l2.2-2.2c.3-.3.7-.4 1-.2 1.1.4 2.3.6 3.6.6.6 0 1 .4 1 1V20c0 .6-.4 1-1 1C10.6 21 3 13.4 3 4c0-.6.4-1 1-1h3.5c.6 0 1 .4 1 1 0 1.3.2 2.5.6 3.6.1.3 0 .7-.2 1L6.6 10.8z"/>
        </svg>
        <span class="contact-text">0064 27 5139427</span>
      </li>
      <li class="contact-item">
        <svg class="contact-icon" viewBox="0 0 24 24" aria-hidden="true">
          <path d="M12 3L2 12h3v9h5v-6h4v6h5v-9h3L12 3z"/>
        </svg>
        <span class="contact-text">www.ostranderthrillers.example</span>
      </li>
      <li class="contact-item">
        <svg class="contact-icon outline" viewBox="0 0 24 24" aria-hidden="true">
          <circle cx="12" cy="12" r="9.5"/>
          <ellipse cx="12" cy="12" rx="4.2" ry="9.5"/>
          <line x1="2.5" y1="12" x2="21.5" y2="12"/>
          <path d="M4.2 7h15.6M4.2 17h15.6"/>
        </svg>
        <span class="contact-text">paulbostrander@mailbox.example</span>
      </li>
    </ul>
  </main>
</body>
</html>
```